Restaurant Email Club Sign Up Poster

Looking for a creative design that will catch people's eye and prompt them to sign up for our email club for our Restaurant that we run in Omaha, Nebraska. Open to any creative ways to most effectively grab peoples attention quickly without being too confusing. Want it to be simple but actionable.

Have attached some documents for your assistance - in addition to some marketing materials we have put out in the past.

Would like to put design on posters to hang up throughout the restaurant and likely will make stickers to put on check presenters as well.

Catchy stock photo or use of the cheese curd photo probably good idea - callout things mentioned in the "must haves" section below. Looking for most creative and catchy, yet simple design.

Target Market(s)

30-50 year olds males and females.

Industry/Entity Type

Restaurant

Requirements
Must have
• Must include callouts for -
• Sign up for E-Club for access to future offers and events (or something along these lines)
• Free Appetizer for Signing Up
• Free Birthday Meal
Should not have
• Please do not make this poster like the postcard that I attached to the project - this is not a poster to call out that we are a new burger and beer spot, that we have 40 rotating taps, or that we have 15 specialty burgers, etc. This is simply a poster to grab someones attention and get them to sign up for our email club. Should maybe have a catchy question, something like, "Want a Free Appetizer?" or something catchy and similar, and then below say "And access to future deals and event happenings?"

```html
<!DOCTYPE html>
<html lang="en">
<head>
<meta charset="utf-8">
<title>E-Club Sign Up Poster</title>
<link href="https://fonts.googleapis.com/css2?family=Arimo:wght@400;700&display=swap" rel="stylesheet">
<style>
  :root {
    --backdrop: #ecebe8;
    --poster-black: #0b0b0c;
    --brand-red: #e3141f;
    --text-white: #ffffff;
    --food-gold: #d98a2a;
    --food-amber: #b4541a;
    --food-deep: #5a230c;
  }
  * { margin: 0; padding: 0; box-sizing: border-box; }
  html, body {
    width: 1200px;
    height: 1149px;
    overflow: hidden;
    background: var(--backdrop);
  }
  body { position: relative; font-family: "Arimo", Arial, sans-serif; }

  .poster {
    position: absolute;
    left: 210px;
    top: 22px;
    width: 780px;
    height: 1105px;
    background:
      radial-gradient(ellipse 300px 380px at 390px 470px, rgba(70,70,74,0.85), rgba(30,30,32,0) 70%),
      linear-gradient(180deg, var(--poster-black) 0%, #141416 45%, var(--poster-black) 100%);
    overflow: hidden;
  }

  .red { color: var(--brand-red); }
  .white { color: var(--text-white); }

  .headline {
    position: absolute;
    left: 131px;
    top: 112px;
    font-weight: 700;
    font-size: 27px;
    line-height: 30px;
  }
  .headline .kicker { letter-spacing: 1px; }

  .divider {
    position: absolute;
    left: 150px;
    top: 250px;
    width: 360px;
    height: 2px;
    background: linear-gradient(90deg, rgba(120,120,120,0), rgba(140,140,140,0.9) 40%, rgba(120,120,120,0));
  }

  .brand {
    position: absolute;
    left: 380px;
    top: 312px;
    display: flex;
    align-items: center;
    gap: 10px;
    font-weight: 700;
    font-size: 24px;
    color: var(--brand-red);
  }
  .brand-dot {
    width: 22px;
    height: 22px;
    border-radius: 50%;
    background: var(--brand-red);
  }

  .food-photo {
    position: absolute;
    left: 240px;
    top: 410px;
    width: 334px;
    height: 290px;
    border-radius: 40% 40% 30% 30%;
    background: radial-gradient(ellipse at 50% 60%, var(--food-gold) 0%, var(--food-amber) 45%, var(--food-deep) 80%, rgba(20,10,5,0) 100%);
  }

  .eclub-callout {
    position: absolute;
    left: 363px;
    top: 757px;
    padding-left: 12px;
    border-left: 4px solid var(--brand-red);
    font-weight: 700;
    font-size: 19px;
    line-height: 25px;
  }

  .offers {
    position: absolute;
    right: 202px;
    top: 895px;
    padding: 8px 14px 10px 0;
    border-right: 4px solid var(--brand-red);
    text-align: right;
    font-weight: 700;
    font-size: 20px;
    line-height: 34px;
  }
</style>
</head>
<body>
  <main class="poster">
    <header class="headline">
      <div class="red kicker">WANT A</div>
      <div class="white">Free Appetizer?</div>
      <div class="red">Join Our E-Club</div>
    </header>

    <div class="divider"></div>

    <div class="brand"><span class="brand-dot"></span><span>Ironhorn Tap</span></div>

    <div class="food-photo" role="img" aria-label="Photo of golden fried cheese curds with melted cheese pulling from one"></div>

    <section class="eclub-callout">
      <div class="red">Sign up for</div>
      <div><span class="white">E-Club</span> <span class="red">for access</span></div>
      <div><span class="red">to future</span> <span class="white">offers and events</span></div>
    </section>

    <section class="offers">
      <div><span class="white">Free</span> <span class="red">Appetizer</span> <span class="white">for Signing Up</span></div>
      <div><span class="white">Free</span> <span class="red">Birthday</span> <span class="white">Meal</span></div>
    </section>
  </main>
</body>
</html>
```